Momentum Personal Training- Signage Design Project

Momentum Personal Training is looking for a signage design for our shop front windows and doors.

We have been in business for 12 years and are moving to a new and bigger premises for a fresh start, so we are feeling energetic, vibrant and excited.

We have 2 windows + 2 doors (photo included but taken at night so slightly dark)

The dimensions of each window are: 2100mm wide x 2660 height
The dimensions of each door is: 740mm wide x 1920mm height

IMPORTANT- If standing on sidewalk looking at the window signage, the right window needs to be partially blocked out. Not completely blocked out but allow an element of privacy for clients so that passers by would really need to concentrate to see in. Im open to suggestions on how this is done.

We also want to advertise our promo which is "$39 p.w Unlimited Personal Training* "

I would like that to stand out but can be on either window or wherever you think.

We would also like the website address potentially included somewhere www.fitbloom-studio.com.au

I have made some notes below as to the kind of signage I think would look good, but im very open to suggestions.

It needs to look vibrant, possibly work in with our logo (attached) and most importantly it must catch the eye.

NOTE- Im open to suggestions and creative flare, im prepared to not necessarily make the logo a big part of the design so feel free to submit designs that dont rely on logo

About Us:

We are a personal training studio in Melbourne

We are somewhat unique for a PT studio in that we will have more equipment and better quality equipment than most of our competitors, but our prices are extremely affordable. Many studios that have these facilities will be charging much higher fees.

We are moving to a new area, for a fresh start and will be aggressively pushing to recruit as many clients as possible. There is a bigger competitor not far from us that has slightly better signage visibility, so we want to stand out.

75% of our clients are female, this tends to be the target demographic. We do however, want to be able to recruit male clients too, so we dont want our signage to suggest its a female gym.

We offer 1on1/Private personal training and small group/indoor bootcamp personal training. We specialise in both, but are probably angling more at the group training market as it offers a higher hourly wage to us + its cheaper for clients to afford.

Our client base is middle class, we dont tend to attract the upper class client.

We offer a very personable service where we know all our clients well and we build strong rapport with them.Our clients arent just number/members, we strive to get to know them personally and show we have a genuine interest in them.

Feel free to ask any questions, I will answer promptly as the deadline is near.

Target Market(s)

females aged 25-45. We wtill want to be able to attract male clients too. People who have been thinking about starting exercise

Industry/Entity Type

Training

Requirements
Must have
• * Should fit in with our logo colours i believe
* Signage must be warm and inviting. (Very important) We want women to be comfortable to come in, not too" hardcore". We do want to still be able to attract male clients too, so not so feminine that men wont feel comfortable.
*If standing on sidewalk looking at the window signage, the right window needs to be partially blocked out. Not completely blocked out but allow an element of privacy for clients so that passers by would really need to concentrate to see in. We also dont want people to feel like they are trapped in a dungeon with no outside light.
* Fresh, energetic
* Needs to catch the eye of motorists
* I dont want the design to look too busy with too much text (Very important)
* personable service where we know all our clients well and we build strong rapport with them.
Nice to have
• Im open to suggestions. I want it to stand out but not be trashy. I want motorists to remember us.
Should not have
• Dont want any designs that are too dark and overtly masculine
Nothing with too much text.
Passing motorist should be able to grasp the concept very quickly. Clear, not confusing.

```html
<!DOCTYPE html>
<html lang="en">
<head>
<meta charset="utf-8">
<title>Momentum Personal Training – Shopfront Signage</title>
<link href="https://fonts.googleapis.com/css2?family=Arimo:wght@400;700&display=swap" rel="stylesheet">
<style>
  :root {
    --canvas: #f2f2f2;
    --panel: #ffffff;
    --panel-edge: #c9c9c9;
    --teal-light: #4fc3d3;
    --teal-mid: #3aa9b8;
    --teal-dark: #27838f;
    --ink: #111111;
    --charcoal: #3a3a3c;
    --white: #ffffff;
    --photo-warm: #b98a68;
    --photo-shadow: #5a4a42;
  }
  * { box-sizing: border-box; margin: 0; padding: 0; }
  html, body { width: 1200px; height: 1200px; overflow: hidden; }
  body {
    background: var(--canvas);
    font-family: "Arimo", Arial, sans-serif;
    position: relative;
  }
  .panel {
    position: absolute;
    background: var(--panel);
    border: 1px solid var(--panel-edge);
    box-shadow: 1px 2px 4px rgba(0,0,0,0.25);
    overflow: hidden;
  }
  .window-left  { left: 30px;  top: 340px; width: 412px; height: 521px; }
  .window-right { left: 760px; top: 340px; width: 410px; height: 521px; }
  .header-sign  { left: 451px; top: 340px; width: 298px; height: 122px; padding: 4px; }
  .door-left    { left: 451px; top: 474px; width: 145px; height: 387px; }
  .door-right   { left: 605px; top: 474px; width: 145px; height: 387px; }

  .band {
    position: absolute;
    left: 0; right: 0;
    top: 182px; height: 201px;
    border-top: 2px solid var(--ink);
    border-bottom: 2px solid var(--ink);
    box-shadow: inset 0 2px 0 var(--white), inset 0 -2px 0 var(--white);
    background: linear-gradient(to bottom, var(--teal-light), var(--teal-mid) 55%, var(--teal-dark));
  }
  .athlete-photo {
    position: absolute;
    left: 0; top: 120px;
    width: 140px; height: 258px;
    background: linear-gradient(160deg, var(--photo-warm), var(--photo-shadow));
  }
  .tagline {
    position: absolute;
    right: 18px; top: 230px;
    color: var(--white);
    font-size: 15.5px;
    line-height: 22px;
    text-align: right;
    white-space: nowrap;
  }

  .header-frame {
    width: 100%; height: 100%;
    border: 2px solid var(--ink);
    display: flex; flex-direction: column; align-items: center; justify-content: center;
    gap: 14px;
  }
  .brand { display: flex; align-items: center; gap: 8px; }
  .brand-dot { width: 14px; height: 14px; border-radius: 50%; background: var(--teal-mid); flex: none; }
  .brand-name { font-size: 18px; color: var(--charcoal); font-weight: 400; white-space: nowrap; }
  .web { font-size: 16px; color: var(--ink); white-space: nowrap; }

  .door-band {
    position: absolute;
    left: 0; right: 0;
    top: 90px; height: 120px;
    background: var(--charcoal);
    color: var(--white);
    display: flex; flex-direction: column; align-items: center; justify-content: center;
    text-align: center;
  }
  .door-brand { font-size: 15px; font-weight: 700; letter-spacing: 0.5px; }
  .hours-title { font-size: 11px; margin-bottom: 3px; }
  .hours-line { font-size: 9.5px; line-height: 13px; }

  .promo {
    position: absolute;
    left: 30px; top: 124px;
    width: 316px; height: 316px;
  }
  .promo-text {
    position: absolute;
    left: 30px; top: 124px;
    width: 316px; height: 316px;
    display: flex; flex-direction: column; align-items: center; justify-content: center;
    color: var(--white);
  }
  .price { font-size: 74px; font-weight: 700; letter-spacing: -1px; line-height: 1; }
  .price sup { font-size: 38px; vertical-align: 28px; margin-right: 2px; }
  .offer { font-size: 20px; margin-top: 14px; }
</style>
</head>
<body>
  <section class="panel window-left">
    <div class="band"></div>
    <div class="athlete-photo" role="img" aria-label="Photo of a woman training on an indoor exercise bike"></div>
    <p class="tagline">Never get so busy making a living<br>that you forget to make a life</p>
  </section>

  <section class="panel header-sign">
    <div class="header-frame">
      <div class="brand">
        <span class="brand-dot"></span>
        <span class="brand-name">Momentum Personal Training</span>
      </div>
      <p class="web">www.fitbloom-studio.com.au</p>
    </div>
  </section>

  <section class="panel door-left">
    <div class="door-band">
      <span class="door-brand">MOMENTUM</span>
    </div>
  </section>

  <section class="panel door-right">
    <div class="door-band">
      <p class="hours-title">HOURS OF OPERATION</p>
      <p class="hours-line">Monday - Sunday</p>
      <p class="hours-line">HH:MM am - MM:MM pm</p>
    </div>
  </section>

  <section class="panel window-right">
    <div class="band"></div>
    <svg class="promo" viewBox="0 0 316 316" aria-hidden="true">
      <defs>
        <linearGradient id="promoFill" x1="0" y1="0" x2="0" y2="1">
          <stop offset="0" stop-color="#4fc3d3"/>
          <stop offset="0.55" stop-color="#3aa9b8"/>
          <stop offset="1" stop-color="#27838f"/>
        </linearGradient>
      </defs>
      <circle cx="158" cy="158" r="156" fill="#111111"/>
      <circle cx="158" cy="158" r="153" fill="#ffffff"/>
      <circle cx="158" cy="158" r="150" fill="url(#promoFill)"/>
    </svg>
    <div class="promo-text">
      <p class="price"><sup>$</sup>39 p.w</p>
      <p class="offer">Unlimited Personal Training</p>
    </div>
  </section>
</body>
</html>
```